BUILDERS MERCHANTS BUSINESS CARD

we need a business card for our long established builders merchants
we supply to both trade and diy
we offer an express delivery service
we would like TRV to standout as this our main trade mark logo
also our main colours are blue/white/yellow

Industry/Entity Type

Trade

Contact Information for Business Card

TRV BUILDERS MERCHANTS

SUPPLIERS OF ALL TYPES OF BUILDING MATERIALS

-SAND/CEMENT
-BRICKS/BLOCKS
-PLASTER/PLASTERBOARDS
-INSULATION
-FENCING/GARDEN PAVING
-PLUMBING
-ELECTRICAL
-EXPRESS DELIVERIES

EST OVER 30 YEARS

418 MARLOWE RISE
LONDON
NORWOOD
SE19 4XD

0208 5294861
0208 5392617
FAX 0208539 7283
EMAIL- TRVBUILDERSMERCHANTS@POSTVALE.CO.UK

```html
<!DOCTYPE html>
<html lang="en">
<head>
<meta charset="utf-8">
<title>TRV Builders Merchant – Business Card</title>
<link rel="stylesheet" href="https://fonts.googleapis.com/css2?family=Lato:wght@400;700;900&display=swap">
<style>
  :root {
    --stage: #2a2a2a;
    --card-white: #ffffff;
    --navy: #232c78;
    --navy-deep: #1a205a;
    --yellow: #f7d61c;
    --yellow-warm: #f2c511;
    --text-light: #ffffff;
  }
  html, body {
    margin: 0;
    width: 1200px;
    height: 1000px;
    overflow: hidden;
    background: var(--stage);
    font-family: "Lato", sans-serif;
  }
  .business-card {
    position: absolute;
    left: 100px;
    top: 215px;
    width: 1000px;
    height: 571px;
    border-radius: 22px;
    overflow: hidden;
    background: var(--card-white);
    box-shadow: 0 20px 50px rgba(0,0,0,0.5);
  }
  .card-bands {
    position: absolute;
    inset: 0;
  }
  .brand {
    position: absolute;
    left: 48px;
    top: 42px;
    color: var(--navy);
  }
  .brand-name {
    display: flex;
    align-items: center;
    gap: 16px;
    font-weight: 900;
    font-size: 104px;
    line-height: 1;
    letter-spacing: 2px;
  }
  .brand-square {
    width: 30px;
    height: 30px;
    background: var(--yellow);
  }
  .brand-tagline {
    margin-top: 6px;
    font-weight: 700;
    font-size: 24px;
    letter-spacing: 2px;
  }
  .established-badge {
    position: absolute;
    right: 90px;
    top: 28px;
    width: 160px;
    height: 160px;
    border-radius: 50%;
    background: radial-gradient(circle, var(--yellow) 55%, var(--yellow-warm) 100%);
  }
  .card-details {
    position: absolute;
    left: 0;
    right: 0;
    top: 300px;
    text-align: center;
    font-size: 22px;
    line-height: 1.25;
    color: var(--text-light);
  }
  .services-heading {
    margin: 0;
    font-weight: 700;
    color: var(--yellow);
    font-size: 22px;
  }
  .services-list {
    margin: 0 0 24px;
  }
  .contact-list {
    margin: 0;
    color: var(--yellow);
  }
  .contact-list p { margin: 0; }
  .contact-label { font-weight: 700; }
</style>
</head>
<body>
  <article class="business-card">
    <svg class="card-bands" width="1000" height="571" viewBox="0 0 1000 571" aria-hidden="true">
      <defs>
        <linearGradient id="navyFill" x1="0" y1="0" x2="0" y2="1">
          <stop offset="0" stop-color="#2b3690"/>
          <stop offset="1" stop-color="#1a205a"/>
        </linearGradient>
      </defs>
      <polygon points="0,262 1000,192 1000,214 0,282" fill="var(--yellow)"/>
      <polygon points="0,280 1000,212 1000,571 0,571" fill="url(#navyFill)"/>
    </svg>

    <div class="brand">
      <div class="brand-name"><span>TRV</span><span class="brand-square"></span></div>
      <div class="brand-tagline">BUILDERS MERCHANT</div>
    </div>

    <div class="established-badge" role="img" aria-label="30 years established rosette badge"></div>

    <div class="card-details">
      <p class="services-heading">Suppliers of All Types of Building Materials:</p>
      <p class="services-list">Sand/Cement, Bricks/Blocks, Plaster/Plasterboards, Insulation,<br>Fencing/Garden Paving, Plumbing Electrical and Express Deliveries.</p>
      <div class="contact-list">
        <p><span class="contact-label">Phone:</span> 0208 5294861</p>
        <p><span class="contact-label">Mobile:</span> 0208 5392617</p>
        <p><span class="contact-label">Fax:</span> 0208539 7283</p>
        <p><span class="contact-label">Email:</span> trvbuildersmerchants@postvale.co.uk</p>
        <p><span class="contact-label">Address:</span> 418 Marlowe Rise, London Norwood SE19 4XD</p>
      </div>
    </div>
  </article>
</body>
</html>
```